Wheels Bring Trade - Two sided invitation to encourage bike friendly businesses

Pedal Haven is a charitable trust who want to grow everyday bike use. One way to do that is help businesses understand that 'Wheels Bring Trade'. We want a postcard sized 'invitation' that bike users can give to their favourite businesses, inviting them to find out more about all the benefits of attracting bike users to their business and becoming a 'Pedal Haven Business'. We are currently finalising copy, so the attached is indicative but not final copy. The docx file is the words, the png is indicative of the type of infographic we might want to feature.
I'm also attaching a mock up of our window sticker for businesses, and some social shares featuring photographic images which we have available to use. This will give you an idea of our branding to date. Our extended branding concept (which we will use when we re-do our website) is based on icons, so I'm open to seeing icon focused designs also.
The feel needs to be inviting, credible, enticing, business like, noticeable, with a strong call to action.

Target Market(s)

Small business operators: retail, cafes, etc; also managers of larger chains such as supermarkets, gyms, etc.

Industry/Entity Type

Non Profit

Font styles to use
Serif
Other font styles liked:
• Logo is done in Raleway, so need compatible font.

Colors
9ccb3b

Requirements
Must have
• Two Sides
• Use the copy provided
• Strong call to action - visiting website
• Use our colours
• A6 sized cards
Nice to have
• Compelling images and/or infographic
• Consistency with circles / curves used in other branding.
Should not have
• Not bland, not something that will get lost on the recipients desk or counter.

```html
<!DOCTYPE html>
<html lang="en">
<head>
<meta charset="utf-8">
<title>Pedal Haven – Invitation Card</title>
<link rel="stylesheet" href="https://fonts.googleapis.com/css2?family=Raleway:wght@400;500;700&display=swap">
<style>
  :root {
    --green: #3db54a;
    --ink: #5a5a5a;
    --panel: #f4f4f4;
    --page: #ffffff;
    --white: #ffffff;
    --photo-warm: #d49a66;
    --photo-deep: #6e4634;
    --photo-light: #f3d7a8;
    --heart: #d8262f;
    --social: #8a8a8a;
  }
  * { box-sizing: border-box; margin: 0; padding: 0; }
  html, body {
    width: 1000px; height: 1200px; overflow: hidden;
    background: var(--page);
    font-family: "Raleway", Arial, sans-serif;
  }
  .card {
    position: absolute; left: 115px; top: 53px;
    width: 770px; height: 1094px;
    background: var(--panel);
    box-shadow: 0 6px 18px rgba(0,0,0,0.18);
    overflow: hidden;
  }
  .hero {
    position: absolute; left: 0; top: 0; width: 770px; height: 547px;
    background:
      radial-gradient(ellipse at 85% 10%, var(--photo-light) 0%, rgba(243,215,168,0) 55%),
      linear-gradient(160deg, #a2553a 0%, var(--photo-warm) 45%, #b98563 70%, var(--photo-deep) 100%);
  }
  .hero-brand {
    position: absolute; left: 412px; top: 40px;
    display: flex; align-items: center; gap: 16px;
  }
  .brand-dot {
    width: 130px; height: 130px; border-radius: 50%;
    background: var(--white); border: 6px solid #777;
  }
  .hero-brand .brand-name {
    font-size: 31px; font-weight: 500; color: var(--white); line-height: 1.05;
  }
  .hero-question {
    position: absolute; left: 390px; top: 256px; width: 350px;
    color: var(--white); font-size: 24px; line-height: 1.2; text-align: center;
  }
  .hashtag {
    position: absolute; left: 430px; top: 438px;
    font-size: 52px; font-weight: 700; color: var(--white);
  }

  .panel-brand {
    position: absolute; left: 48px; top: 575px;
    display: flex; align-items: center; gap: 10px;
  }
  .panel-brand .brand-dot { width: 95px; height: 95px; border-width: 5px; }
  .panel-brand .brand-name { font-size: 22px; font-weight: 500; color: var(--green); line-height: 1.05; }

  .benefit-icons {
    position: absolute; left: 403px; top: 590px;
    display: flex; gap: 20px;
  }
  .benefit-icons svg { width: 65px; height: 65px; display: block; }

  .why {
    position: absolute; left: 45px; top: 681px; width: 700px;
    color: var(--ink);
  }
  .section-title { font-size: 26px; font-weight: 700; color: var(--green); margin-left: 25px; line-height: 1.1; }
  .benefits { list-style: none; font-size: 19px; line-height: 22.5px; margin-top: 1px; }
  .benefits li { position: relative; padding-left: 25px; }
  .benefits li .tick { position: absolute; left: 0; top: 4px; width: 17px; height: 15px; }
  .heart { display: inline-block; width: 26px; height: 19px; vertical-align: -3px; margin: 0 4px; }
  .study { font-size: 19px; line-height: 22.5px; margin: 13px 0 0 25px; }
  .num { color: var(--green); }

  .just-think { position: absolute; left: 70px; top: 910px; }
  .just-think .section-title, .cta .section-title { margin: 0; }
  .just-think p, .cta p { font-size: 19px; line-height: 22px; color: var(--ink); }
  .just-think .hl { color: var(--green); }

  .cta { position: absolute; left: 70px; top: 993px; }

  .social { position: absolute; left: 523px; top: 978px; list-style: none; }
  .social li { font-size: 19px; line-height: 22px; color: var(--ink); display: flex; align-items: center; gap: 3px; }
  .social-dot { width: 16px; height: 16px; border-radius: 50%; background: var(--social); display: inline-block; }
</style>
</head>
<body>
<main class="card">
  <section class="hero" role="img" aria-label="Warm sunlit photo of a cyclist riding a road bike along a city footpath">
    <div class="hero-brand">
      <span class="brand-dot"></span>
      <span class="brand-name">Pedal<br>Haven</span>
    </div>
    <p class="hero-question">Why make biking customers<br>- and their $$$ - welcome at<br>your business?</p>
    <p class="hashtag">#ipedaltoo</p>
  </section>

  <div class="panel-brand">
    <span class="brand-dot"></span>
    <span class="brand-name">Pedal<br>Haven</span>
  </div>

  <div class="benefit-icons">
    <svg viewBox="0 0 65 65" aria-label="Spending">
      <circle cx="32.5" cy="32.5" r="32.5" fill="var(--green)"/>
      <circle cx="32.5" cy="32.5" r="17" fill="none" stroke="#fff" stroke-width="5" stroke-dasharray="80 8"/>
      <text x="32.5" y="39" text-anchor="middle" font-family="Raleway, sans-serif" font-weight="700" font-size="17" fill="#fff">$</text>
    </svg>
    <svg viewBox="0 0 65 65" aria-label="Bike parking">
      <circle cx="32.5" cy="32.5" r="32.5" fill="var(--green)"/>
      <rect x="17" y="17" width="31" height="31" rx="4" fill="none" stroke="#fff" stroke-width="3"/>
      <text x="25" y="38" text-anchor="middle" font-family="Raleway, sans-serif" font-weight="700" font-size="18" fill="#fff">P</text>
      <circle cx="35" cy="40" r="3.5" fill="none" stroke="#fff" stroke-width="1.5"/>
      <circle cx="43" cy="40" r="3.5" fill="none" stroke="#fff" stroke-width="1.5"/>
      <path d="M35 40 L38 34 L43 40 M38 34 H42" fill="none" stroke="#fff" stroke-width="1.5"/>
    </svg>
    <svg viewBox="0 0 65 65" aria-label="Cafe">
      <circle cx="32.5" cy="32.5" r="32.5" fill="var(--green)"/>
      <path d="M19 31 H42 V37 A10 9 0 0 1 19 37 Z" fill="#fff"/>
      <path d="M42 33 A4 4 0 0 1 42 41" fill="none" stroke="#fff" stroke-width="2.5"/>
      <ellipse cx="31" cy="48" rx="15" ry="2.5" fill="#fff"/>
      <path d="M26 27 q-3 -4 0 -8 M31 27 q-3 -4 0 -8 M36 27 q-3 -4 0 -8" fill="none" stroke="#fff" stroke-width="2"/>
    </svg>
    <svg viewBox="0 0 65 65" aria-label="Bicycle">
      <circle cx="32.5" cy="32.5" r="32.5" fill="var(--green)"/>
      <circle cx="20" cy="38" r="8" fill="none" stroke="#fff" stroke-width="2.5"/>
      <circle cx="45" cy="38" r="8" fill="none" stroke="#fff" stroke-width="2.5"/>
      <path d="M20 38 L28 26 H42 L45 38 M28 26 L33 38 L42 26 M26 22 H31 M42 26 L40 20 H45" fill="none" stroke="#fff" stroke-width="2.5" stroke-linejoin="round"/>
    </svg>
  </div>

  <section class="why">
    <h2 class="section-title">Why welcome bikes?</h2>
    <ul class="benefits">
      <li><svg class="tick" viewBox="0 0 17 15"><path d="M1 8 L6 13 L16 2" fill="none" stroke="var(--green)" stroke-width="3"/></svg>Biking customers spend $$$ where parking’s easy.</li>
      <li><svg class="tick" viewBox="0 0 17 15"><path d="M1 8 L6 13 L16 2" fill="none" stroke="var(--green)" stroke-width="3"/></svg>They spend $$$ locally as they must carry what they buy.</li>
      <li><svg class="tick" viewBox="0 0 17 15"><path d="M1 8 L6 13 L16 2" fill="none" stroke="var(--green)" stroke-width="3"/></svg>Biking customers move slower, so see what your business offers.</li>
      <li><svg class="tick" viewBox="0 0 17 15"><path d="M1 8 L6 13 L16 2" fill="none" stroke="var(--green)" stroke-width="3"/></svg>They tell friends where’s good to park and shop, where they feel welcome.</li>
      <li><svg class="tick" viewBox="0 0 17 15"><path d="M1 8 L6 13 L16 2" fill="none" stroke="var(--green)" stroke-width="3"/></svg>You’re helping people be environmentally, budget and heart friendly – and<br>they’ll<svg class="heart" viewBox="0 0 24 18"><path d="M12 16 C4 10 2 7 4 4 C6 1 10 2 12 5 C14 2 18 1 20 4 C22 7 20 10 12 16 Z" fill="none" stroke="var(--heart)" stroke-width="1.8"/></svg>you for it.</li>
    </ul>
    <p class="study">A Melbourne study showed swapping a car park for six bike parks<br>could increase the space’s retail spend from <span class="num">$27</span> to <span class="num">$97.20</span> an hour.</p>
  </section>

  <section class="just-think">
    <h2 class="section-title">Just think</h2>
    <p><span class="hl">every bike</span> parked by someone else’s<br>business <span class="hl">could have been your customer.</span></p>
  </section>

  <section class="cta">
    <h2 class="section-title">pedalhaven.org</h2>
    <p>to see how you can become<br>a pedal haven business.</p>
  </section>

  <ul class="social">
    <li><span class="social-dot"></span>/Pedal Haven</li>
    <li><span class="social-dot"></span>/@PedalHaven</li>
    <li><span class="social-dot"></span>/Pedal Haven</li>
    <li><span class="social-dot"></span>/PedalHaven</li>
  </ul>
</main>
</body>
</html>
```